Webdesign für Zirkeltraining für Frauen
Zielgruppe
zirkeltraining für Frauen.
Frauen jeden Alters ... 18-85 Jahre.
Aufgabenstellung
Bitte in den Farben der Bilder und der Logos bleiben. Klare Struktur. Logo wird gerade vom designer Final bearbeitet und liegt daher nur als Beispiel dem Briefing bei.

```html
<!DOCTYPE html>
<html lang="de">
<head>
<meta charset="utf-8">
<title>Vitalia – Buchung</title>
<link href="https://fonts.googleapis.com/css2?family=Montserrat:wght@300;400;500;600;700&display=swap" rel="stylesheet">
<style>
:root{
  --blue:#27acdc;
  --blue-soft:#dff1fa;
  --blue-halo:#d4eef9;
  --ink:#1f1f1f;
  --muted:#9a9a9a;
  --line:#e6eef2;
  --white:#ffffff;
  --hero-a:#6b4a2f;
  --hero-b:#c19a6b;
  --hero-c:#3a2a20;
}
*{box-sizing:border-box;margin:0;padding:0}
html,body{width:1200px;height:3438px;overflow:hidden;background:var(--white)}
body{font-family:"Montserrat",sans-serif;color:var(--ink);position:relative}
.screen{position:absolute;left:31px;width:1137px;height:800px;background:var(--white);box-shadow:0 2px 10px rgba(0,0,0,.12);overflow:hidden}

/* navigation */
.nav{position:absolute;left:0;top:0;width:100%;height:53px;background:var(--white)}
.brand{position:absolute;left:42px;top:13px;text-align:center}
.brand-name{display:block;font-size:19px;font-weight:300;letter-spacing:6px;color:var(--ink);line-height:1}
.brand-sub{display:block;font-size:6px;letter-spacing:1px;color:var(--muted);margin-top:3px}
.menu a{position:absolute;top:19px;font-size:13px;color:var(--ink);text-decoration:none}
.social{position:absolute;width:9px;height:9px;border:1.5px solid #555;border-radius:50%;top:22px}

/* hero */
.hero{position:absolute;left:0;top:53px;width:100%;height:167px;background:linear-gradient(100deg,var(--hero-c) 0%,var(--hero-a) 25%,var(--hero-b) 55%,var(--hero-a) 75%,var(--hero-c) 100%)}
.hero-title{position:absolute;left:166px;top:106px;font-size:31px;font-weight:600;color:var(--white)}

/* steps */
.steps{position:absolute;left:0;top:240px;width:100%;height:50px}
.step{position:absolute;width:80px;margin-left:-40px;text-align:center}
.step .halo{position:absolute;left:27px;top:0;width:26px;height:26px;border-radius:50%;background:var(--blue-halo)}
.step .dot{position:absolute;left:38px;top:11px;width:4px;height:4px;border-radius:50%;background:var(--blue)}
.step .label{position:absolute;left:0;top:32px;width:80px;font-size:7.5px;letter-spacing:.5px;color:var(--muted)}
.step.active .label{color:#333;font-weight:500}
.step-line{position:absolute;top:12px;height:1px;background:#c8e3ee}

/* order */
.order-item{position:absolute;left:288px;width:484px;height:63px;border:1.5px solid var(--line)}
.order-title{position:absolute;left:17px;top:18px;font-size:11px;font-weight:600;color:var(--blue)}
.order-sub{position:absolute;left:17px;top:36px;font-size:7px;color:var(--blue)}
.order-select{position:absolute;top:20px;height:16px;border-bottom:1px solid var(--blue);font-size:7px;color:var(--blue);padding-top:3px}
.order-select::after{content:"";position:absolute;right:2px;top:5px;border:2.5px solid transparent;border-top-color:var(--blue)}
.order-price{position:absolute;right:17px;top:25px;font-size:11px;font-weight:600;color:var(--blue)}
.total{position:absolute;left:288px;top:484px;width:484px;height:35px;background:var(--blue-soft);font-size:11px;font-weight:600;color:var(--blue)}
.total span{position:absolute;top:12px}
.btn-small{position:absolute;left:477px;top:576px;width:70px;height:23px;border:1.5px solid var(--blue);font-size:8px;color:#333;text-align:center;line-height:20px;background:var(--white)}

/* forms */
.form-title{position:absolute;top:300px;font-size:20px;font-weight:500;color:var(--ink)}
.field-label{position:absolute;font-size:8px;font-weight:600;color:#333}
.field{position:absolute;height:36px;border:1.5px solid var(--blue);font-size:10px;color:#444;padding:0 12px;line-height:33px;white-space:nowrap}
.field.select::after{content:"";position:absolute;right:12px;top:13px;width:5px;height:5px;border-right:1.5px solid var(--blue);border-bottom:1.5px solid var(--blue);transform:rotate(45deg)}
.faded{opacity:.32}
.faded .field,.faded .pay-option,.faded .brand-box{border-color:#c5d6dd}
.faded .form-title{color:#777}
.brand-box{position:absolute;height:36px;border:1.5px solid var(--blue);text-align:center;font-size:15px;font-weight:700;color:var(--blue);line-height:33px}
.pay-option{position:absolute;left:816px;width:153px;height:69px;border:1.5px solid var(--blue);box-shadow:0 1px 6px rgba(39,172,220,.15);text-align:center}
.card-icon{position:absolute;left:58px;top:23px;width:38px;height:24px;border-radius:3px;background:var(--blue)}
.card-icon::after{content:"";position:absolute;left:0;top:6px;width:100%;height:4px;background:var(--white)}
.card-icon::before{content:"";position:absolute;left:5px;top:14px;width:14px;height:3px;background:var(--white)}
.pay-name{position:absolute;left:0;top:26px;width:100%;font-size:14px;font-weight:700;color:var(--blue)}
.btn-next{position:absolute;left:611px;top:441px;width:138px;height:46px;border:1.5px solid var(--blue);background:var(--white);color:var(--blue);font-size:14px;font-weight:500;text-align:center;line-height:43px;box-shadow:0 1px 6px rgba(0,0,0,.08)}
.btn-order{position:absolute;left:779px;top:557px;width:190px;height:55px;background:var(--blue);color:var(--white);font-size:12.5px;font-weight:600;text-align:center;line-height:15px;padding-top:12px;border-radius:2px}

/* thanks */
.thanks{position:absolute;left:249px;top:273px;width:639px;height:296px;border:2px solid #8fd2ec}
.thanks-badge{position:absolute;left:528px;top:232px;width:80px;height:80px;border-radius:50%;background:var(--white);border:1.5px solid var(--blue-soft)}
.thanks-badge .inner{position:absolute;left:18px;top:18px;width:42px;height:42px;border-radius:50%;border:1.5px solid #bfe6f5}
.thanks-badge .core{position:absolute;left:33px;top:33px;width:12px;height:12px;border-radius:50%;background:var(--blue)}
.thanks-brand{position:absolute;left:0;top:62px;width:100%;text-align:center}
.thanks-brand .brand-name{font-size:32px;letter-spacing:10px}
.thanks-brand .brand-sub{font-size:9px;letter-spacing:2px;margin-top:5px}
.thanks-title{position:absolute;left:0;top:142px;width:100%;text-align:center;font-size:23px;font-weight:500;line-height:29px}
.thanks-text{position:absolute;left:110px;top:224px;width:419px;text-align:center;font-size:11px;line-height:13px;color:#333}

/* footer */
.footer{position:absolute;left:0;top:640px;width:100%;height:160px;background:var(--blue);color:var(--white)}
.foot-col{position:absolute;top:41px}
.foot-col h4{font-size:11px;font-weight:600;line-height:13px;margin-bottom:16px}
.foot-col p{font-size:9px;line-height:11px}
.foot-col.links p{font-style:italic}
.foot-social{position:absolute;top:45px;width:9px;height:9px;border:1.5px solid var(--white);border-radius:50%}
</style>
</head>
<body>

<!-- Screen 1: Order -->
<section class="screen" style="top:37px">
  <header class="nav">
    <div class="brand"><span class="brand-name">VITALIA</span><span class="brand-sub">Studio für Frauen</span></div>
    <nav class="menu"><a style="left:257px">Startseite</a><a style="left:376px">Trainingskonzept</a><a style="left:549px">Mitgliedschaften</a><a style="left:713px">Aktuelles</a><a style="left:824px">Kontakt</a></nav>
    <span class="social" style="left:979px"></span><span class="social" style="left:1005px"></span><span class="social" style="left:1032px"></span><span class="social" style="left:1059px"></span>
  </header>
  <div class="hero" role="img" aria-label="Foto: Frau beim Dehnen auf einer Yogamatte im hellen Studio"><h1 class="hero-title">Buchung</h1></div>
  <div class="steps">
    <span class="step-line" style="left:441px;width:171px"></span>
    <div class="step active" style="left:441px"><span class="halo"></span><span class="dot"></span><span class="label">ORDER</span></div>
    <div class="step" style="left:527px"><span class="dot"></span><span class="label">SHIPPING</span></div>
    <div class="step" style="left:612px"><span class="dot"></span><span class="label">PAYMENT</span></div>
  </div>
  <div class="order-item" style="top:321px">
    <span class="order-title">Vitalia Mitgliedschaft</span>
    <span class="order-sub">Standard Mitgliedschaft</span>
    <span class="order-select" style="left:148px;width:140px">Standard</span>
    <span class="order-select" style="left:308px;width:59px">1</span>
    <span class="order-price">20€ / Monat</span>
  </div>
  <div class="order-item" style="top:396px">
    <span class="order-title">Workshop</span>
    <span class="order-sub">Fitness &amp; Ernährung</span>
    <span class="order-select" style="left:308px;width:59px">1</span>
    <span class="order-price">Einmalig 30€</span>
  </div>
  <div class="total"><span style="left:17px">Gesamt</span><span style="right:17px">50€</span></div>
  <div class="btn-small">Weiter</div>
  <footer class="footer">
    <div class="foot-col" style="left:336px"><h4>Kontakt</h4><p>+49 0361 204718<br>info@vitalia-studio.de<br>Lindenweg 12<br>99084 Erfurt</p></div>
    <div class="foot-col links" style="left:513px"><h4>Sitelinks</h4><p>Das Trainingskonzept<br>Unsere Mitgliedschaften<br>Unser Blog<br>Was ist Zirkeltraining</p></div>
    <div class="foot-col" style="left:705px"><h4>Informationen /<br>Aktuelles</h4><p style="margin-top:-13px">Blogbeitrag 1<br>Blogbeitrag 2<br>Blogbeitrag 3<br>Blogbeitrag 4</p></div>
    <span class="foot-social" style="left:1063px"></span><span class="foot-social" style="left:1083px"></span><span class="foot-social" style="left:1103px"></span>
  </footer>
</section>

<!-- Screen 2: Shipping -->
<section class="screen" style="top:929px">
  <header class="nav">
    <div class="brand"><span class="brand-name">VITALIA</span><span class="brand-sub">Studio für Frauen</span></div>
    <nav class="menu"><a style="left:257px">Startseite</a><a style="left:376px">Trainingskonzept</a><a style="left:549px">Mitgliedschaften</a><a style="left:713px">Aktuelles</a><a style="left:824px">Kontakt</a></nav>
    <span class="social" style="left:979px"></span><span class="social" style="left:1005px"></span><span class="social" style="left:1032px"></span><span class="social" style="left:1059px"></span>
  </header>
  <div class="hero" role="img" aria-label="Foto: Frau beim Dehnen auf einer Yogamatte im hellen Studio"><h1 class="hero-title">Buchung</h1></div>
  <div class="steps">
    <span class="step-line" style="left:441px;width:171px"></span>
    <div class="step" style="left:441px"><span class="dot"></span><span class="label">ORDER</span></div>
    <div class="step active" style="left:527px"><span class="halo"></span><span class="dot"></span><span class="label">SHIPPING</span></div>
    <div class="step" style="left:612px"><span class="dot"></span><span class="label">PAYMENT</span></div>
  </div>
  <div class="shipping-form">
    <h2 class="form-title" style="left:167px">Bestellinformationen</h2>
    <span class="field-label" style="left:167px;top:349px">Voller Name</span>
    <div class="field" style="left:167px;top:361px;width:253px">Jana Weber</div>
    <span class="field-label" style="left:167px;top:417px">ADRESSE</span>
    <div class="field" style="left:167px;top:429px;width:253px">Lindenweg 12</div>
    <span class="field-label" style="left:167px;top:484px">Stadt</span>
    <span class="field-label" style="left:297px;top:484px">Postleitzahl</span>
    <div class="field" style="left:167px;top:497px;width:124px">Erfurt</div>
    <div class="field" style="left:297px;top:497px;width:123px">99084</div>
    <span class="field-label" style="left:167px;top:552px">Land</span>
    <div class="field select" style="left:167px;top:565px;width:253px">Deutschland</div>
  </div>
  <div class="payment-form faded">
    <h2 class="form-title" style="left:497px">Kreditkarteninformationen</h2>
    <span class="field-label" style="left:497px;top:349px">Kartennummer</span>
    <div class="field" style="left:497px;top:361px;width:168px">1234 5678 3456 2456</div>
    <div class="brand-box" style="left:673px;top:361px;width:78px">KARTIX</div>
    <span class="field-label" style="left:497px;top:417px">Name des Karteninhaber</span>
    <div class="field" style="left:497px;top:429px;width:254px">Jana Weber</div>
    <span class="field-label" style="left:497px;top:484px">Auslaufdatum</span>
    <div class="field select" style="left:497px;top:497px;width:254px">05 / 21</div>
    <span class="field-label" style="left:497px;top:552px">CVV</span>
    <div class="field" style="left:497px;top:565px;width:124px">123</div>
    <div class="pay-option" style="top:360px"><span class="card-icon"></span></div>
    <div class="pay-option" style="top:459px"><span class="pay-name">Penniva</span></div>
  </div>
  <div class="btn-next">Weiter</div>
  <footer class="footer">
    <div class="foot-col" style="left:336px"><h4>Kontakt</h4><p>+49 0361 204718<br>info@vitalia-studio.de<br>Lindenweg 12<br>99084 Erfurt</p></div>
    <div class="foot-col links" style="left:513px"><h4>Sitelinks</h4><p>Das Trainingskonzept<br>Unsere Mitgliedschaften<br>Unser Blog<br>Was ist Zirkeltraining</p></div>
    <div class="foot-col" style="left:705px"><h4>Informationen /<br>Aktuelles</h4><p style="margin-top:-13px">Blogbeitrag 1<br>Blogbeitrag 2<br>Blogbeitrag 3<br>Blogbeitrag 4</p></div>
    <span class="foot-social" style="left:1063px"></span><span class="foot-social" style="left:1083px"></span><span class="foot-social" style="left:1103px"></span>
  </footer>
</section>

<!-- Screen 3: Payment -->
<section class="screen" style="top:1757px">
  <header class="nav">
    <div class="brand"><span class="brand-name">VITALIA</span><span class="brand-sub">Studio für Frauen</span></div>
    <nav class="menu"><a style="left:257px">Startseite</a><a style="left:376px">Trainingskonzept</a><a style="left:549px">Mitgliedschaften</a><a style="left:713px">Aktuelles</a><a style="left:824px">Kontakt</a></nav>
    <span class="social" style="left:979px"></span><span class="social" style="left:1005px"></span><span class="social" style="left:1032px"></span><span class="social" style="left:1059px"></span>
  </header>
  <div class="hero" role="img" aria-label="Foto: Frau beim Dehnen auf einer Yogamatte im hellen Studio"><h1 class="hero-title">Buchung</h1></div>
  <div class="steps">
    <span class="step-line" style="left:441px;width:171px"></span>
    <div class="step" style="left:441px"><span class="dot"></span><span class="label">ORDER</span></div>
    <div class="step" style="left:527px"><span class="dot"></span><span class="label">SHIPPING</span></div>
    <div class="step active" style="left:612px"><span class="halo"></span><span class="dot"></span><span class="label">PAYMENT</span></div>
  </div>
  <div class="shipping-form faded">
    <h2 class="form-title" style="left:167px">Bestellinformationen</h2>
    <span class="field-label" style="left:167px;top:349px">Voller Name</span>
    <div class="field" style="left:167px;top:361px;width:253px">Jana Weber</div>
    <span class="field-label" style="left:167px;top:417px">ADRESSE</span>
    <div class="field" style="left:167px;top:429px;width:253px">Lindenweg 12</div>
    <span class="field-label" style="left:167px;top:484px">Stadt</span>
    <span class="field-label" style="left:297px;top:484px">Postleitzahl</span>
    <div class="field" style="left:167px;top:497px;width:124px">Erfurt</div>
    <div class="field" style="left:297px;top:497px;width:123px">99084</div>
    <span class="field-label" style="left:167px;top:552px">Land</span>
    <div class="field select" style="left:167px;top:565px;width:253px">Deutschland</div>
  </div>
  <div class="payment-form">
    <h2 class="form-title" style="left:497px">Kreditkarteninformationen</h2>
    <span class="field-label" style="left:497px;top:349px">Kartennummer</span>
    <div class="field" style="left:497px;top:361px;width:168px">1234 5678 3456 2456</div>
    <div class="brand-box" style="left:673px;top:361px;width:78px">KARTIX</div>
    <span class="field-label" style="left:497px;top:417px">Name des Karteninhaber</span>
    <div class="field" style="left:497px;top:429px;width:254px">Jana Weber</div>
    <span class="field-label" style="left:497px;top:484px">Auslaufdatum</span>
    <div class="field select" style="left:497px;top:497px;width:254px">05 / 21</div>
    <span class="field-label" style="left:497px;top:552px">CVV</span>
    <div class="field" style="left:497px;top:565px;width:124px">123</div>
    <div class="pay-option" style="top:360px"><span class="card-icon"></span></div>
    <div class="pay-option" style="top:459px"><span class="pay-name">Penniva</span></div>
    <div class="btn-order">Jetzt zahlungspflichtig<br>bestellen</div>
  </div>
  <footer class="footer">
    <div class="foot-col" style="left:336px"><h4>Kontakt</h4><p>+49 0361 204718<br>info@vitalia-studio.de<br>Lindenweg 12<br>99084 Erfurt</p></div>
    <div class="foot-col links" style="left:513px"><h4>Sitelinks</h4><p>Das Trainingskonzept<br>Unsere Mitgliedschaften<br>Unser Blog<br>Was ist Zirkeltraining</p></div>
    <div class="foot-col" style="left:705px"><h4>Informationen /<br>Aktuelles</h4><p style="margin-top:-13px">Blogbeitrag 1<br>Blogbeitrag 2<br>Blogbeitrag 3<br>Blogbeitrag 4</p></div>
    <span class="foot-social" style="left:1063px"></span><span class="foot-social" style="left:1083px"></span><span class="foot-social" style="left:1103px"></span>
  </footer>
</section>

<!-- Screen 4: Confirmation -->
<section class="screen" style="top:2609px">
  <header class="nav">
    <div class="brand"><span class="brand-name">VITALIA</span><span class="brand-sub">Studio für Frauen</span></div>
    <nav class="menu"><a style="left:257px">Startseite</a><a style="left:376px">Trainingskonzept</a><a style="left:549px">Mitgliedschaften</a><a style="left:713px">Aktuelles</a><a style="left:824px">Kontakt</a></nav>
    <span class="social" style="left:979px"></span><span class="social" style="left:1005px"></span><span class="social" style="left:1032px"></span><span class="social" style="left:1059px"></span>
  </header>
  <div class="hero" role="img" aria-label="Foto: Frau beim Dehnen auf einer Yogamatte im hellen Studio"><h1 class="hero-title">Buchung</h1></div>
  <div class="thanks">
    <div class="thanks-brand"><span class="brand-name">VITALIA</span><span class="brand-sub">Studio für Frauen</span></div>
    <h2 class="thanks-title">Wir bedanken uns für Ihre<br>Bestellung und freuen uns mit</h2>
    <p class="thanks-text">Weiter Informationen bezüglich der Trainingszeiten und was Sie zum Training brauchen, bekommen Sie per E-Mail zugesendet.</p>
  </div>
  <div class="thanks-badge"><span class="inner"></span><span class="core"></span></div>
  <footer class="footer">
    <div class="foot-col" style="left:336px"><h4>Kontakt</h4><p>+49 0361 204718<br>info@vitalia-studio.de<br>Lindenweg 12<br>99084 Erfurt</p></div>
    <div class="foot-col links" style="left:513px"><h4>Sitelinks</h4><p>Das Trainingskonzept<br>Unsere Mitgliedschaften<br>Unser Blog<br>Was ist Zirkeltraining</p></div>
    <div class="foot-col" style="left:705px"><h4>Informationen /<br>Aktuelles</h4><p style="margin-top:-13px">Blogbeitrag 1<br>Blogbeitrag 2<br>Blogbeitrag 3<br>Blogbeitrag 4</p></div>
    <span class="foot-social" style="left:1063px"></span><span class="foot-social" style="left:1083px"></span><span class="foot-social" style="left:1103px"></span>
  </footer>
</section>

</body>
</html>
```